We need an attractive business card design that is modern and inviting. We like the blue and yellow (or gold) colors that are displayed with the logo. The business should communicate trust, experience, and integrity.

Target Market(s)

Residential and Commercial

Industry/Entity Type

Business

Contact Information for Business Card

Recessed Lighting
LED Retro Fit
Sign Repair
Alarms and Cameras
Mobile Home Services
24hr service calls

Font styles to use
Serif
Sans Serif

Colors
3176b5
0455a3
fece3e
fbee3e

Requirements
Must have
• Brondle Electric
• Owner: Marcus Tivane
• Licensed and Insured
• TECL #58917
Nice to have
• Exquisite Detail!!
• Over 20 years of experience
Should not have
• Nothing boring or traditional!!!

```html
<!DOCTYPE html>
<html lang="en">
<head>
<meta charset="utf-8">
<title>Brondle Electric – Business Card</title>
<link href="https://fonts.googleapis.com/css2?family=Montserrat:wght@400;500;600;700&display=swap" rel="stylesheet">
<style>
  :root {
    --brand-blue: #0b57a3;
    --brand-yellow: #f2ea22;
    --paper: #ffffff;
    --backdrop: #e4e4e4;
  }
  * { margin: 0; padding: 0; box-sizing: border-box; }
  html, body {
    width: 1200px; height: 843px; overflow: hidden;
    background: var(--backdrop);
    font-family: "Montserrat", sans-serif;
  }
  .canvas { position: relative; width: 1200px; height: 843px; }
  .card {
    position: absolute; top: 252px;
    width: 536px; height: 320px;
    border-radius: 14px; overflow: hidden;
  }
  .card-front { left: 40px; background: var(--paper); color: var(--brand-blue); }
  .card-back { left: 625px; background: var(--brand-blue); color: var(--paper); }
  .ring { position: absolute; inset: 0; }

  .front-title {
    position: absolute; left: 29px; top: 28px;
    font-size: 35px; font-weight: 600; letter-spacing: 0.5px; line-height: 1;
  }
  .word-accent { color: var(--brand-yellow); margin-left: 10px; }
  .front-tagline {
    position: absolute; left: 31px; top: 73px;
    font-size: 19.5px; font-weight: 400; letter-spacing: 0.6px;
  }
  .front-tagline strong { font-weight: 600; }
  .owner-name {
    position: absolute; left: 31px; top: 155px;
    font-size: 20px; font-weight: 600; letter-spacing: 0.4px;
  }
  .owner-role { position: absolute; left: 31px; top: 180px; font-size: 13.5px; }
  .address { position: absolute; left: 31px; top: 205px; font-size: 13.5px; line-height: 18px; }
  .contacts { position: absolute; left: 31px; top: 247px; list-style: none; font-size: 13.5px; line-height: 17.5px; }
  .contacts li { display: flex; align-items: center; gap: 8px; }
  .contacts svg { width: 9px; height: 9px; }
  .licence { position: absolute; left: 287px; top: 282px; font-size: 13.5px; }

  .back-mark {
    position: absolute; left: 319px; top: 40px;
    width: 72px; height: 72px; border-radius: 50%;
    border: 4px solid var(--paper);
  }
  .back-title {
    position: absolute; left: 0; width: 100%; padding-left: 210px; top: 116px;
    font-size: 30px; font-weight: 600; letter-spacing: 0.5px; line-height: 1;
    white-space: nowrap;
  }
  .back-title .word-accent { margin-left: 8px; }
  .service-list {
    position: absolute; left: 210px; top: 164px;
    list-style: none; font-size: 13.8px; line-height: 17.4px;
  }
  .service-list li { display: flex; align-items: center; gap: 9px; }
  .service-list li::before {
    content: ""; width: 7px; height: 7px; border-radius: 50%;
    background: var(--brand-yellow);
  }
</style>
</head>
<body>
<main class="canvas">

  <section class="card card-front" aria-label="Card front">
    <svg class="ring" viewBox="0 0 536 320" aria-hidden="true">
      <circle cx="534" cy="159" r="139" fill="none" stroke="var(--brand-blue)" stroke-width="25"/>
    </svg>
    <h1 class="front-title">BRONDLE<span class="word-accent">ELECTRIC</span></h1>
    <p class="front-tagline"><strong>OVER 20</strong> YEARS OF EXPERIENCE</p>
    <h2 class="owner-name">MARCUS TIVANE</h2>
    <p class="owner-role">Owner</p>
    <p class="address">31875 w 12 oak Rd<br>Ferndale mi 48220</p>
    <ul class="contacts">
      <li><svg viewBox="0 0 10 10"><path d="M2 1h2l1 2-1.2 1a5 5 0 0 0 2.2 2.2L7 5l2 1v2a1 1 0 0 1-1 1A7 7 0 0 1 1 2a1 1 0 0 1 1-1z" fill="currentColor"/></svg>+330 2718-4093</li>
      <li><svg viewBox="0 0 10 10"><rect x="0.5" y="2" width="9" height="6" fill="none" stroke="currentColor"/><path d="M0.5 2l4.5 3.5L9.5 2" fill="none" stroke="currentColor"/></svg>info@brondleelectric.com</li>
      <li><svg viewBox="0 0 10 10"><circle cx="5" cy="5" r="4.3" fill="none" stroke="currentColor"/><path d="M0.7 5h8.6M5 0.7c-2.5 2.5-2.5 6.1 0 8.6M5 0.7c2.5 2.5 2.5 6.1 0 8.6" fill="none" stroke="currentColor" stroke-width="0.8"/></svg>www.brondleelectric.com</li>
    </ul>
    <p class="licence">TECL #58917</p>
  </section>

  <section class="card card-back" aria-label="Card back">
    <svg class="ring" viewBox="0 0 536 320" aria-hidden="true">
      <circle cx="0" cy="159" r="150" fill="none" stroke="var(--paper)" stroke-width="20"/>
    </svg>
    <div class="back-mark" aria-hidden="true"></div>
    <h2 class="back-title">BRONDLE<span class="word-accent">ELECTRIC</span></h2>
    <ul class="service-list">
      <li>Residential and Commercial</li>
      <li>Recessed Lighting</li>
      <li>LED Retro Fit</li>
      <li>Sign Repair</li>
      <li>Alarms and Cameras</li>
      <li>Mobile Home Services</li>
      <li>24hr service calls</li>
    </ul>
  </section>

</main>
</body>
</html>
```